Design a landing page

We have a logo, we have colours in mind. What we need is to create a typical one-page landing page that would look nicely on both PC and mobile devices/tablets.

Typical layout - logo top left, top right - shop/client area buttons (links will open to different websites), informational area in the middle - image on the left + text on the right then image on the right + text on the left etc., then text links at the bottom (T&S, Cookie policy, privacy policy etc.).

Page must have cookie notification as per EU law.

We will also need help in preparing photos/images (up to 8) for the website.

End result should be either a Wordpress theme (preferred - so we can install it from wordpress control panel) or HTML/CSS page source. All scripts/images/files should be included - no external links to js/image libraries please.

The photo of the device attached. Primary users will be home users with placement on the ceiling, Minority of users will be business/commercial users with wall placements. Device is meant to monitor climat in the premises (Temperature, humidity, dew point) and alert users if readings are not within allowed range.

Need extra days to review

Industry/Entity Type

Microclimate Monitoring in premises

Coding

Coded - Design and coding required

Number of Pages Required

1 page

Colors
0054AA
0677BA
7BADD7
CADEEF
E8F1F8
0094D4
00A9DD
6FCCEA
C7EBF8
E9F6FB

Requirements
Must have
• White background, layout as described unless better option offered and accepted. Must have cookie warning.

```html
<!DOCTYPE html>
<html lang="en">
<head>
<meta charset="UTF-8">
<title>Climora – Monitor Your Indoor Climate</title>
<link rel="stylesheet" href="https://fonts.googleapis.com/css2?family=Arimo:wght@400;700&display=swap">
<style>
  :root {
    --brand-blue: #0054AA;
    --action-blue: #00A9DD;
    --hero-bg: #E8F1F8;
    --panel-blue: #CADEEF;
    --panel-sky: #C7EBF8;
    --photo-ceiling: #a9aaa6;
    --photo-chart: #eef0f2;
    --ink: #000000;
    --white: #ffffff;
    --logo-ink: #0f2a4a;
  }
  * { box-sizing: border-box; margin: 0; padding: 0; }
  html, body {
    width: 1200px;
    height: 645px;
    overflow: hidden;
    background: var(--white);
    font-family: "Arimo", Arial, sans-serif;
    color: var(--ink);
  }
  .site-header {
    height: 83px;
    background: var(--brand-blue);
    position: relative;
  }
  .brand {
    position: absolute;
    left: 86px;
    top: 14px;
    width: 100px;
    height: 50px;
    background: var(--white);
    border-radius: 8px;
    display: flex;
    align-items: center;
    justify-content: center;
    font-weight: 700;
    font-size: 19px;
    color: var(--logo-ink);
    text-decoration: none;
  }
  .header-actions {
    position: absolute;
    right: 40px;
    top: 21px;
    display: flex;
    gap: 12px;
  }
  .btn {
    display: inline-flex;
    align-items: center;
    justify-content: center;
    height: 36px;
    padding: 0 19px;
    background: var(--action-blue);
    color: var(--white);
    font-size: 16px;
    border-radius: 3px;
    text-decoration: none;
  }
  .btn--active {
    outline: 2px solid var(--white);
    outline-offset: 0;
    box-shadow: 0 0 0 3px #0b1d33;
  }
  .hero {
    height: 337px;
    background: var(--hero-bg);
    position: relative;
  }
  .hero-copy {
    position: absolute;
    left: 86px;
    top: 78px;
    width: 520px;
  }
  .hero-title {
    font-size: 31px;
    font-weight: 700;
    line-height: 1.1;
  }
  .hero-text {
    font-size: 16px;
    line-height: 1.2;
  }
  .hero .btn {
    position: absolute;
    left: 96px;
    top: 258px;
  }
  .hero-media {
    position: absolute;
    left: 638px;
    top: 52px;
    width: 522px;
    height: 240px;
    background: var(--panel-blue);
  }
  .hero-photo {
    position: absolute;
    left: 139px;
    top: 0;
    width: 244px;
    height: 100%;
    background: linear-gradient(160deg, #d9dad6 0%, var(--photo-ceiling) 70%, #6f6c66 100%);
  }
  .feature {
    height: 225px;
    position: relative;
  }
  .feature-media {
    position: absolute;
    left: 86px;
    top: 30px;
    width: 523px;
    height: 175px;
    background: var(--panel-sky);
    border-bottom: 2px solid #a9d3e6;
  }
  .feature-photo {
    position: absolute;
    left: 0;
    top: 0;
    width: 390px;
    height: 100%;
    background: linear-gradient(90deg, var(--photo-chart) 0%, #f1d2cc 45%, #e0775a 75%, #d9a88a 100%);
  }
  .feature-copy {
    position: absolute;
    left: 638px;
    top: 98px;
  }
  .feature-title {
    font-size: 22px;
    font-weight: 700;
    line-height: 1.1;
  }
  .feature-text {
    font-size: 16px;
    line-height: 1.2;
  }
</style>
</head>
<body>
  <header class="site-header">
    <a class="brand" href="#">Climora</a>
    <nav class="header-actions">
      <a class="btn btn--active" href="#">Shop</a>
      <a class="btn" href="#">Client Area</a>
    </nav>
  </header>

  <section class="hero">
    <div class="hero-copy">
      <h1 class="hero-title">Monitor Your Indoor Climate</h1>
      <p class="hero-text">Track temperature, humidity, and dew point in real time. Stay safe and comfortable with intelligent alerts.</p>
    </div>
    <a class="btn" href="#">Learn More</a>
    <div class="hero-media">
      <div class="hero-photo" role="img" aria-label="Hand pressing a climate sensor mounted on a ceiling next to a glass pendant lamp"></div>
    </div>
  </section>

  <section class="feature">
    <div class="feature-media">
      <div class="feature-photo" role="img" aria-label="Dashboard screens showing a temperature chart and a climate heat map"></div>
    </div>
    <div class="feature-copy">
      <h2 class="feature-title">Real-Time Monitoring</h2>
      <p class="feature-text">Get instant updates on climate conditions inside your premises.</p>
    </div>
  </section>
</body>
</html>
```